Brightpath Gym Harlow (Annual sale ONLY $8.95 per week!)

We are after a new fresh design for our annual promo! we need a design that can be used for core flute signs (1200 x 2400), Facebook posts, Instagram posts, posters and any advertising we do throughout our 12 week campaign!

In the past we have gone for a suit all vibe when it comes to advertising with images of people training and looking happy and excited. As we pride ourselves in being a gym for everyone.

Information and text that need to be included in the designs.
Please include logo on each design (attached) also happy with logo color's to be changed to suit designs.

We normally do 2 x core flute designs, one that has the picture and information regarding the sale and another big bold one that shows 50% off to really grab the eye of passing traffic.
Core flute #1
- $8.95 per week*
- Only 100 memberships available!
- Terms and conditions apply*

Core flute #2
- 50% OFF sale
- Annual sale
- Pay nothing for 30 days!

Poster (use in club and local businesses
- $8.95 per week*
- No Joining fees
- 24/7 access

Facebook and Instagram posts
- 50% OFF
- $8.95 per week*
- No joining fees

```html
<!DOCTYPE html>
<html lang="en">
<head>
<meta charset="utf-8">
<title>Brightpath Gym – Annual Sale Campaign</title>
<link rel="stylesheet" href="https://fonts.googleapis.com/css2?family=Barlow+Condensed:ital,wght@1,800;1,900&family=Poppins:wght@400;500;700&display=swap">
<style>
:root{
  --board:#efefef;
  --ink:#222222;
  --black:#0c0c0c;
  --panel:#141414;
  --panel-2:#1e1e1e;
  --red:#e3151c;
  --red-deep:#a20c10;
  --white:#ffffff;
  --rule:#4a4a4a;
}
*{margin:0;padding:0;box-sizing:border-box}
html,body{width:1200px;height:2400px;overflow:hidden;background:var(--board)}
body{font-family:'Poppins',sans-serif;color:var(--white);position:relative}

.board-label{position:absolute;width:400px;text-align:center;font:400 30px/1 'Poppins',sans-serif;color:var(--ink)}

.piece{position:absolute;overflow:hidden;background:linear-gradient(160deg,#242424 0%,var(--panel) 45%,var(--black) 100%);box-shadow:0 10px 24px rgba(0,0,0,.28)}
.piece > *{position:absolute}

.brand{display:flex;align-items:center;gap:8px;white-space:nowrap}
.brand-dot{border-radius:50%;background:var(--red);flex:none}
.brand-name{font-weight:700;color:var(--white);letter-spacing:-.3px}

.display{font-family:'Barlow Condensed',sans-serif;font-style:italic;font-weight:900;line-height:.9;white-space:nowrap}
.red{color:var(--red)}
.outline{color:transparent;-webkit-text-stroke:1.6px var(--white)}
.rule{height:1px;background:var(--rule)}
.centered{left:0;right:0;text-align:center}
.copy{white-space:nowrap;line-height:1}
.photo{border-radius:0}

/* flute sign 1 */
.flute-one{left:242px;top:158px;width:290px;height:581px}
.member-pill{display:flex;border-radius:14px;overflow:hidden;font-size:14px;line-height:22px;border:2px solid var(--red)}
.member-pill .left{background:var(--white);color:var(--black);padding:0 10px}
.member-pill .right{background:var(--red);color:var(--white);font-weight:700;padding:0 10px}

/* flute sign 2 */
.flute-two{left:662px;top:158px;width:290px;height:581px}
.spaced{letter-spacing:14px}

/* poster */
.poster{left:287px;top:848px;width:626px;height:811px}
.poster-band{left:0;top:528px;width:400px;height:140px;background:var(--panel-2)}
.access-icon{width:44px;height:44px}

/* social posts */
.social{top:1781px;width:484px;height:484px}
.facebook{left:81px}
.instagram{left:643px}
.sale-badge{width:130px;height:130px}
</style>
</head>
<body>

<div class="board-label" style="left:187px;top:98px">Flute signs 1</div>
<div class="board-label" style="left:610px;top:98px">Flute signs 2</div>
<div class="board-label" style="left:400px;top:797px">Poster</div>
<div class="board-label" style="left:123px;top:1725px">Facebook</div>
<div class="board-label" style="left:688px;top:1725px">Instagram</div>

<!-- Flute sign 1 -->
<section class="piece flute-one">
  <div class="photo" role="img" aria-label="Photo of a smiling woman and man back to back holding dumbbells in front of a red circle" style="left:0;top:285px;width:290px;height:296px;background:radial-gradient(circle at 50% 45%,var(--red) 0 42%,transparent 43%),linear-gradient(180deg,#3a3a3a,#111)"></div>
  <div class="brand" style="left:62px;top:32px"><span class="brand-dot" style="width:40px;height:40px"></span><span class="brand-name" style="font-size:21px">Brightpath Gym</span></div>
  <div class="display red centered" style="top:92px;font-size:72px">$8.95</div>
  <div class="copy centered" style="top:153px;font-size:24px">per week*</div>
  <div class="rule" style="left:25px;right:25px;top:189px"></div>
  <div class="display centered" style="top:198px;font-size:52px"><span class="outline">ONLY</span> <span class="red">100</span></div>
  <div class="member-pill" style="left:24px;top:249px"><span class="left">Memberships</span><span class="right">AVAILABLE!</span></div>
  <div class="copy centered" style="top:540px;font-size:11px">Terms and conditions apply*</div>
</section>

<!-- Flute sign 2 -->
<section class="piece flute-two">
  <svg style="left:0;top:430px" width="290" height="151" viewBox="0 0 290 151" aria-hidden="true">
    <polygon points="0,30 120,92 0,140" fill="#3a3a3a"/>
    <polygon points="0,140 290,20 290,151 0,151" fill="var(--red-deep)"/>
    <polygon points="60,151 290,50 290,151" fill="var(--red)"/>
  </svg>
  <div class="brand" style="left:72px;top:28px"><span class="brand-dot" style="width:36px;height:36px"></span><span class="brand-name" style="font-size:19px">Brightpath Gym</span></div>
  <div class="display red" style="left:74px;top:78px;font-size:82px">50%</div>
  <div class="copy" style="left:176px;top:128px;font-size:20px">OFF</div>
  <div class="copy" style="left:74px;top:152px;font-size:34px;letter-spacing:16px">SALE</div>
  <div class="rule" style="left:25px;right:25px;top:191px"></div>
  <div class="display outline centered" style="top:202px;font-size:62px">ANNUAL</div>
  <div class="display red centered" style="top:256px;font-size:64px">SALE</div>
  <div class="rule" style="left:25px;right:25px;top:322px"></div>
  <div class="copy centered" style="top:338px;font-size:23px"><b>Pay</b> nothing for</div>
  <div class="copy red centered" style="top:364px;font-size:88px;font-weight:700">30</div>
  <div class="copy centered spaced" style="top:440px;font-size:23px;padding-left:12px">DAYS!</div>
</section>

<!-- Poster -->
<section class="piece poster">
  <div class="photo" role="img" aria-label="Photo of a trainer spotting a woman doing a seated shoulder press on a bench, set against a large red circle" style="left:330px;top:110px;width:296px;height:701px;background:radial-gradient(circle at 85% 38%,var(--red) 0 38%,transparent 39%),linear-gradient(180deg,#3a3a3a,#141414)"></div>
  <div class="poster-band"></div>
  <div class="brand" style="left:47px;top:55px;gap:14px"><span class="brand-dot" style="width:70px;height:70px"></span><span class="brand-name" style="font-size:42px">Brightpath Gym</span></div>
  <div class="display red" style="left:48px;top:165px;font-size:80px">$8.95</div>
  <div class="copy" style="left:246px;top:196px;font-size:30px">per week*</div>
  <div class="rule" style="left:48px;width:300px;top:254px"></div>
  <div class="copy" style="left:48px;top:268px;font-size:28px"><b>Pay</b> nothing for</div>
  <div class="copy red" style="left:48px;top:300px;font-size:28px;font-weight:700">30 days!</div>
  <div class="rule" style="left:48px;width:300px;top:340px"></div>
  <div class="copy" style="left:48px;top:354px;font-size:37px">No Joining</div>
  <div class="display red" style="left:48px;top:392px;font-size:66px">FEES</div>
  <div class="rule" style="left:48px;width:300px;top:456px"></div>
  <svg class="access-icon" style="left:48px;top:470px" viewBox="0 0 44 44" aria-hidden="true">
    <path d="M22 3a19 19 0 1 1-17 10" fill="none" stroke="var(--red)" stroke-width="3"/>
    <text x="4" y="20" font-family="Poppins" font-size="13" font-weight="700" fill="var(--red)">24</text>
    <line x1="18" y1="32" x2="28" y2="14" stroke="var(--red)" stroke-width="2"/>
    <text x="24" y="38" font-family="Poppins" font-size="13" font-weight="700" fill="var(--red)">7</text>
  </svg>
  <div class="copy" style="left:100px;top:466px;font-size:42px">access</div>
  <div class="display" style="left:48px;top:540px;font-size:54px"><span class="outline">ONLY</span> <span class="red">100</span></div>
  <div class="copy" style="left:48px;top:596px;font-size:30px">Memberships</div>
  <div class="copy" style="left:48px;top:626px;font-size:30px;font-weight:700">AVAILABLE!</div>
  <div class="copy" style="left:51px;top:692px;font-size:17px;line-height:1.25;white-space:normal;width:200px">Terms and conditions apply*</div>
</section>

<!-- Facebook post -->
<section class="piece social facebook">
  <svg style="left:0;top:0" width="484" height="484" viewBox="0 0 484 484" aria-hidden="true">
    <polygon points="210,0 345,0 484,150 484,300" fill="var(--red-deep)"/>
    <polygon points="345,0 360,0 484,130 484,150" fill="#555"/>
    <polygon points="360,0 484,0 484,130" fill="var(--red)"/>
  </svg>
  <div class="photo" role="img" aria-label="Photo of a muscular man and a woman training with fiery glowing sparks" style="left:250px;top:120px;width:234px;height:364px;background:radial-gradient(circle at 30% 70%,#e08a1a 0 8%,transparent 22%),linear-gradient(180deg,#5a3a30,#1a1210)"></div>
  <div class="brand" style="left:37px;top:40px"><span class="brand-dot" style="width:36px;height:36px"></span><span class="brand-name" style="font-size:20px">Brightpath Gym</span></div>
  <svg class="sale-badge" style="left:265px;top:62px" viewBox="0 0 130 130" aria-hidden="true"><circle cx="65" cy="65" r="64" fill="var(--red)"/><circle cx="65" cy="65" r="52" fill="var(--white)"/></svg>
  <div class="display" style="left:281px;top:98px;font-size:54px;color:var(--black)">50%</div>
  <div class="copy" style="left:345px;top:140px;font-size:12px;color:var(--black)">OFF</div>
  <div class="copy" style="left:36px;top:102px;font-size:27px">Pay nothing for</div>
  <div class="copy red" style="left:36px;top:132px;font-size:27px;font-weight:700">30 days!</div>
  <div class="rule" style="left:36px;width:210px;top:166px"></div>
  <div class="display red" style="left:36px;top:172px;font-size:60px">$8.95</div>
  <div class="copy" style="left:37px;top:228px;font-size:21px">per week*</div>
  <div class="rule" style="left:36px;width:210px;top:263px"></div>
  <div class="copy" style="left:38px;top:270px;font-size:27px">No Joining</div>
  <div class="display red" style="left:36px;top:300px;font-size:48px">FEES</div>
  <div class="rule" style="left:36px;width:210px;top:350px"></div>
  <div class="display" style="left:34px;top:358px;font-size:38px"><span class="outline">ONLY</span> <span class="red">100</span></div>
  <div class="copy" style="left:34px;top:394px;font-size:21px">Memberships</div>
  <div class="copy" style="left:34px;top:418px;font-size:21px;font-weight:700">AVAILABLE!</div>
</section>

<!-- Instagram post -->
<section class="piece social instagram">
  <svg style="left:0;top:0" width="484" height="484" viewBox="0 0 484 484" aria-hidden="true">
    <polygon points="210,0 345,0 484,150 484,300" fill="var(--red-deep)"/>
    <polygon points="345,0 360,0 484,130 484,150" fill="#555"/>
    <polygon points="360,0 484,0 484,130" fill="var(--red)"/>
  </svg>
  <div class="photo" role="img" aria-label="Photo of a muscular man and a woman training with fiery glowing sparks" style="left:250px;top:120px;width:234px;height:364px;background:radial-gradient(circle at 30% 70%,#e08a1a 0 8%,transparent 22%),linear-gradient(180deg,#5a3a30,#1a1210)"></div>
  <div class="brand" style="left:37px;top:40px"><span class="brand-dot" style="width:36px;height:36px"></span><span class="brand-name" style="font-size:20px">Brightpath Gym</span></div>
  <svg class="sale-badge" style="left:265px;top:62px" viewBox="0 0 130 130" aria-hidden="true"><circle cx="65" cy="65" r="64" fill="var(--red)"/><circle cx="65" cy="65" r="52" fill="var(--white)"/></svg>
  <div class="display" style="left:281px;top:98px;font-size:54px;color:var(--black)">50%</div>
  <div class="copy" style="left:345px;top:140px;font-size:12px;color:var(--black)">OFF</div>
  <div class="copy" style="left:36px;top:102px;font-size:27px">Pay nothing for</div>
  <div class="copy red" style="left:36px;top:132px;font-size:27px;font-weight:700">30 days!</div>
  <div class="rule" style="left:36px;width:210px;top:166px"></div>
  <div class="display red" style="left:36px;top:172px;font-size:60px">$8.95</div>
  <div class="copy" style="left:37px;top:228px;font-size:21px">per week*</div>
  <div class="rule" style="left:36px;width:210px;top:263px"></div>
  <div class="copy" style="left:38px;top:270px;font-size:27px">No Joining</div>
  <div class="display red" style="left:36px;top:300px;font-size:48px">FEES</div>
  <div class="rule" style="left:36px;width:210px;top:350px"></div>
  <div class="display" style="left:34px;top:358px;font-size:38px"><span class="outline">ONLY</span> <span class="red">100</span></div>
  <div class="copy" style="left:34px;top:394px;font-size:21px">Memberships</div>
  <div class="copy" style="left:34px;top:418px;font-size:21px;font-weight:700">AVAILABLE!</div>
</section>

</body>
</html>
```